Building company requiring web site design

We need a web design for a new company based in Sydney called Kestrel Building Co. We build and renovate new and existing homes for consumers. We would like to see design that use the colours red and grey. The final design should communicate innovative building but with old fashion quality, great customer service and attention to detail. I have already had a logo and stationary design completed and would like to use the these colour schemes
Updates

Target Market(s)

Home owners, investors

Industry/Entity Type

Building

Coding

Coded - Design and coding required

Number of Pages Required

5+ page

Requirements
Must have
• Home page, contact page, about us page, gallery page and testimonial page
Nice to have
• Contact form

```html
<!DOCTYPE html>
<html lang="en">
<head>
<meta charset="utf-8">
<title>Kestrel Building Co</title>
<link href="https://fonts.googleapis.com/css2?family=Lato:ital,wght@0,400;0,700;0,900;1,400&family=Roboto+Slab:wght@400;700&display=swap" rel="stylesheet">
<style>
:root{
  --red:#b8403f;
  --red-dark:#9c3433;
  --ink:#222222;
  --charcoal:#2b2b2b;
  --grey:#8f8f8f;
  --band:#3e4046;
  --white:#ffffff;
  --text:#333333;
}
*{margin:0;padding:0;box-sizing:border-box}
html,body{width:1200px;height:2990px;overflow:hidden;background:var(--white)}
body{position:relative;font-family:"Lato",sans-serif;color:var(--text)}
.abs{position:absolute}
.brand{display:flex;align-items:center;gap:10px;font-family:"Lato",sans-serif;font-weight:900;color:var(--ink);white-space:nowrap}
.brand .mark{width:22px;height:22px;background:var(--red);flex:none}

/* social dots */
.social{display:flex}
.social span{border-radius:50%;background:var(--red);border:2px solid var(--white);box-shadow:0 0 0 1px rgba(255,255,255,.6)}

/* header */
.header{left:0;top:0;width:1200px;height:156px;border-bottom:3px solid var(--red)}
.header .brand{position:absolute;left:88px;top:66px;font-size:28px}
.topbar{left:430px;top:0;width:770px;height:38px;background:var(--charcoal);display:flex;align-items:center;padding-left:18px;gap:24px;color:var(--white);font-size:18px;font-weight:700}
.topbar .sep{width:1px;height:20px;background:#777}
.topbar .social{gap:8px;margin-left:10px}
.topbar .social span{width:26px;height:26px}
.topbar svg{vertical-align:-3px;margin-right:8px}
.nav{left:480px;top:78px;display:flex;align-items:center;font-weight:700;font-size:17px;color:var(--ink)}
.nav a{color:inherit;text-decoration:none;padding:8px 22px;border-right:1px solid #ccc}
.nav a:last-child{border-right:0}
.nav a.active{background:var(--red);color:var(--white);border-radius:3px;margin-right:24px;border-right:0}

/* hero */
.hero{left:0;top:159px;width:1200px;height:609px;background:linear-gradient(180deg,#3f86d8 0%,#8dbbe8 18%,#c4b79f 30%,#a99378 52%,#8a735c 66%,#5d8f32 78%,#3f7a22 100%)}
.hero h1{position:absolute;left:88px;top:232px;font-family:"Roboto Slab",serif;font-weight:700;font-size:40px;line-height:56px;color:var(--white);text-shadow:0 2px 4px rgba(0,0,0,.55)}
.helpform{position:absolute;left:712px;top:136px;width:420px;height:420px;border-radius:50%;background:rgba(255,255,255,.5)}
.helpform h2{position:absolute;left:58px;top:62px;font-family:"Roboto Slab",serif;font-size:25px;font-weight:700;color:var(--ink)}
.field{position:absolute;height:34px;background:var(--white);border:1px solid #ccc;font-size:13px;color:#555;padding:9px 10px}
.field.select::after{content:"";position:absolute;right:10px;top:14px;border:5px solid transparent;border-top:6px solid var(--red)}
.submit{position:absolute;left:134px;top:290px;width:150px;height:54px;background:#111;color:var(--white);font-family:"Roboto Slab",serif;font-weight:700;font-size:24px;display:flex;align-items:center;justify-content:center}

/* about */
.about{left:0;top:768px;width:1200px;height:472px;background:linear-gradient(90deg,#ececec,#f7f7f7 60%,#e8e8e8)}
.band{left:0;top:1240px;width:1200px;height:248px;background:var(--band)}
.sec-title{position:absolute;display:flex;align-items:baseline;gap:14px;font-size:42px;font-weight:700;color:var(--ink)}
.sec-title .red{color:var(--red)}
.rule{position:absolute;height:2px;background:#bcbcbc}
.about .sec-title .brand{font-size:26px}
.about p{position:absolute;left:88px;top:140px;width:596px;font-size:13.5px;line-height:23px;color:#333}
.readmore{position:absolute;left:88px;top:286px;font-size:14px;font-weight:900;color:var(--red-dark)}
.about-art{position:absolute;left:724px;top:40px;width:452px;height:250px;border-radius:6px;background:linear-gradient(180deg,#c2463f 0%,#c2463f 28%,#d9c39c 29%,#d9c39c 62%,#e2e2e2 63%,#cfcfcf 100%)}

.service{position:absolute;top:1100px;width:282px;height:340px}
.service .face{position:absolute;left:0;top:0;width:282px;height:266px;display:flex;align-items:center;justify-content:center}
.service .side{position:absolute;left:282px;top:0;width:46px;height:340px;background:linear-gradient(180deg,rgba(0,0,0,.12),rgba(0,0,0,.3));clip-path:polygon(0 0,100% 20%,100% 100%,0 100%)}
.service .label{position:absolute;left:0;top:266px;width:282px;height:74px;background:linear-gradient(180deg,#111,#2a2a2a);color:var(--white);font-weight:700;font-size:24px;line-height:28px;text-align:center;padding-top:10px}

/* testimonials */
.quote{left:88px;top:1632px;width:900px;height:108px;background:#efefef;clip-path:polygon(0 0,96% 0,100% 20%,100% 100%,0 100%);padding:14px 60px 0 50px;font-size:13px;font-style:italic;line-height:24px;color:#444}
.quote::before{content:"\201C";position:absolute;left:18px;top:2px;font-size:40px;color:#bbb;font-style:normal}
.avatar{left:962px;top:1620px;width:120px;height:120px;border-radius:50%;border:5px solid var(--white);box-shadow:0 0 0 1px #ccc;background:#b9a08c}
.dots{left:88px;top:1750px;display:flex;gap:6px}
.dots span{width:9px;height:9px;border-radius:50%;background:#888}
.dots span:first-child{background:var(--red)}
.author{left:734px;top:1750px;font-size:13px;font-style:italic;color:var(--red)}

/* gallery */
.gallery{left:0;top:1824px;width:1200px;height:516px;background:var(--red)}
.gallery .sec-title{left:0;width:1200px;justify-content:center;top:40px;font-size:40px;color:var(--white)}
.gallery .sec-title .dark{color:#111}
.tile{position:absolute}
.arrow{position:absolute;top:286px;width:32px;height:36px;background:rgba(0,0,0,.35);display:flex;align-items:center;justify-content:center}

/* consultation */
.consult{left:86px;top:2400px;width:1032px;height:280px;background:linear-gradient(90deg,#2c2a28 0%,#4a3d31 50%,#6f5b47 100%)}
.consult h3{position:absolute;left:52px;top:38px;font-size:48px;font-weight:700;color:var(--white);letter-spacing:.5px}
.consult p{position:absolute;left:52px;top:108px;font-size:28px;line-height:36px;color:var(--white)}
.consult .tel{position:absolute;left:52px;top:190px;display:flex;align-items:center;gap:14px;font-size:40px;font-weight:700;color:#d8474a}
.consult .tel .ring{width:46px;height:46px;border-radius:50%;border:2px solid var(--white);display:flex;align-items:center;justify-content:center}

/* footer */
.footer-col{position:absolute;top:2740px}
.footer-col h4{font-size:16px;font-weight:700;color:var(--red);padding-bottom:10px;border-bottom:1px solid #ccc;width:200px}
.links{list-style:none;margin-top:16px;font-size:13px;line-height:28px;color:#333}
.links li::before{content:"\203A";margin-right:12px;color:#888}
.contact{margin-top:14px;font-size:13px;line-height:18px;color:#333}
.contact .row{display:flex;gap:14px;margin-bottom:18px}
.map{margin-top:14px;width:226px;height:124px;border:1px solid #ccc;background:#e4e6d8}
.footer-brand{position:absolute;left:930px;top:2846px;font-size:21px}
.bottombar{left:0;top:2940px;width:1200px;height:50px;background:var(--red)}
.bottombar .dark{position:absolute;left:680px;top:0;width:520px;height:50px;background:#1a1a1a;clip-path:polygon(50px 0,100% 0,100% 100%,0 100%)}
.bottombar .copy{position:absolute;left:88px;top:16px;font-size:13px;font-weight:700;color:var(--white)}
.bottombar .social{position:absolute;left:1006px;top:10px;gap:12px}
.bottombar .social span{width:30px;height:30px}
</style>
</head>
<body>

<div class="abs header">
  <div class="brand"><span class="mark"></span>Kestrel Building Co</div>
</div>

<div class="abs topbar">
  <span>ABN 41 502 883 219</span><span class="sep"></span>
  <span>Licence # 518304k</span><span class="sep"></span>
  <span><svg width="16" height="16" viewBox="0 0 24 24"><path fill="#fff" d="M6.6 10.8a15 15 0 006.6 6.6l2.2-2.2c.3-.3.7-.4 1-.2 1.1.4 2.3.6 3.6.6.6 0 1 .4 1 1V20c0 .6-.4 1-1 1A17 17 0 013 4c0-.6.4-1 1-1h3.5c.6 0 1 .4 1 1 0 1.3.2 2.5.6 3.6.1.3 0 .7-.2 1z"/></svg>02-5550-1487</span>
  <span class="social"><span></span><span></span><span></span></span>
</div>

<nav class="abs nav">
  <a class="active">Home</a><a>About Us</a><a>Gallery</a><a>Testimonials</a><a>Contact Us</a>
</nav>

<section class="abs hero" role="img" aria-label="Photo of a large two-storey stone and timber family home with a green lawn under a blue sky">
  <h1>Planning To Build<br>Or Renovate A House ?</h1>
  <div class="helpform">
    <h2>How We Can Help You?</h2>
    <div class="field" style="left:36px;top:98px;width:344px">Name</div>
    <div class="field" style="left:36px;top:142px;width:344px">Email</div>
    <div class="field" style="left:36px;top:186px;width:168px">Phone</div>
    <div class="field select" style="left:212px;top:186px;width:168px">Budget</div>
    <div class="field select" style="left:36px;top:230px;width:168px">Service Type</div>
    <div class="field select" style="left:212px;top:230px;width:168px">Comments</div>
    <div class="submit">SUBMIT</div>
  </div>
</section>

<section class="abs about">
  <div class="sec-title" style="left:88px;top:44px"><span class="red">About</span><span class="brand">Kestrel Building Co.</span></div>
  <div class="rule" style="left:88px;top:110px;width:588px"></div>
  <p>Lorem ipsum dolor sit amet, consectetuer adipiscing elit, sed diam nonummy nibh euismod tincidunt ut laoreet dolore magna aliquam erat volutpat. Ut wisi enim ad minim veniam, quis nostrud exerci tation ullamcorper suscipit lobortis nisl ut aliquip ex ea commodo consequat. Duis autem vel eum iriure dolor in hendrerit in vulputate velit esse molestie consequat, vel illum dolore eu feugiat nulla facilisis at vero eros et accumsan et iusto odio dignissim.</p>
  <div class="readmore">READ MORE</div>
  <div class="about-art" role="img" aria-label="Illustration of a model house with a red roof resting on rolled building plans"></div>
</section>
<div class="abs band"></div>

<div class="service" style="left:86px">
  <div class="side"></div>
  <div class="face" style="background:var(--red)">
    <svg width="90" height="130" viewBox="0 0 90 130"><rect x="8" y="6" width="74" height="122" fill="#fff"/><g fill="#b8403f"><rect x="18" y="18" width="12" height="12"/><rect x="39" y="18" width="12" height="12"/><rect x="60" y="18" width="12" height="12"/><rect x="18" y="40" width="12" height="12"/><rect x="39" y="40" width="12" height="12"/><rect x="60" y="40" width="12" height="12"/><rect x="18" y="62" width="12" height="12"/><rect x="39" y="62" width="12" height="12"/><rect x="60" y="62" width="12" height="12"/><rect x="18" y="84" width="12" height="12"/><rect x="60" y="84" width="12" height="12"/><rect x="36" y="100" width="18" height="28"/></g></svg>
  </div>
  <div class="label">Building<br>Repairs</div>
</div>
<div class="service" style="left:462px">
  <div class="side"></div>
  <div class="face" style="background:#2b2b2b">
    <svg width="150" height="110" viewBox="0 0 150 110" fill="#fff"><circle cx="75" cy="22" r="18"/><path d="M45 80c0-20 14-32 30-32s30 12 30 32z"/><circle cx="36" cy="54" r="16"/><path d="M8 108c0-18 12-28 28-28s28 10 28 28z"/><circle cx="114" cy="54" r="16"/><path d="M86 108c0-18 12-28 28-28s28 10 28 28z"/></svg>
  </div>
  <div class="label">Construction<br>Management</div>
</div>
<div class="service" style="left:838px">
  <div class="side"></div>
  <div class="face" style="background:var(--grey)">
    <svg width="130" height="120" viewBox="0 0 130 120" fill="#fff"><path d="M10 18l30-12 16 14-8 10 66 72-12 12-66-70-10 8z"/><path d="M108 8a22 22 0 00-26 28L14 100l12 12 66-66a22 22 0 0028-26l-14 12-12-4-4-12z"/></svg>
  </div>
  <div class="label">Renovation<br>Services</div>
</div>

<div class="sec-title" style="left:88px;top:1526px;font-size:40px"><span><span class="red">Client</span> Testimonials</span></div>
<div class="rule" style="left:88px;top:1590px;width:588px"></div>
<div class="abs quote">Lorem sum dolor sit amet, consectetuer adipiscing elit, sed diam nonummy nibh euismod tincidunt ut laoreet re agn aliqam erat volutpat wisi enim ad minim veniam, quis nostrud exerci tation ullamcorper suscipit lobortis nisl ut aliquip modo conseuatis autem vel eum iriure dolor in hendrerit in vulputate velit esse molestie consequat, vel illum dolore eu.</div>
<div class="abs avatar" role="img" aria-label="Portrait photo of a client"></div>
<div class="abs dots"><span></span><span></span><span></span></div>
<div class="abs author">Marcus Hale, Northgate Homes , AU</div>

<section class="abs gallery">
  <div class="sec-title"><span>Work <span class="dark">Gallery</span></span></div>
  <div class="rule" style="left:420px;top:102px;width:480px;background:rgba(255,255,255,.4)"></div>
  <div class="tile" style="left:86px;top:140px;width:262px;height:328px;background:#ebe7e0" role="img" aria-label="Bright white living room with arched ceiling"></div>
  <div class="tile" style="left:352px;top:140px;width:188px;height:160px;background:#5a3628" role="img" aria-label="Timber interior under renovation"></div>
  <div class="tile" style="left:352px;top:304px;width:188px;height:164px;background:#8c6a50" role="img" aria-label="Workers laying timber flooring"></div>
  <div class="tile" style="left:544px;top:140px;width:334px;height:136px;background:#b5a488" role="img" aria-label="Builders reviewing plans on site"></div>
  <div class="tile" style="left:544px;top:280px;width:334px;height:188px;background:linear-gradient(180deg,#86acd8 0%,#86acd8 35%,#b08a60 36%,#8a6e50 100%)" role="img" aria-label="New timber home with scaffolding"></div>
  <div class="tile" style="left:882px;top:140px;width:236px;height:328px;background:linear-gradient(180deg,#8a5a34 0%,#8a5a34 30%,#dcd6cc 31%,#e8e4dc 100%)" role="img" aria-label="Kitchen with exposed ceiling beams"></div>
  <div class="arrow" style="left:22px"><svg width="10" height="14"><path d="M8 1L2 7l6 6" stroke="#fff" stroke-width="2" fill="none"/></svg></div>
  <div class="arrow" style="left:1146px"><svg width="10" height="14"><path d="M2 1l6 6-6 6" stroke="#fff" stroke-width="2" fill="none"/></svg></div>
</section>

<section class="abs consult" role="img" aria-label="Desk with building plans, safety glasses and a yellow hard hat">
  <h3>FREE CONSULTATION</h3>
  <p>Get Free Consultation Call Us Today For<br>An Appointment</p>
  <div class="tel"><span class="ring"><svg width="22" height="22" viewBox="0 0 24 24"><path fill="#fff" d="M6.6 10.8a15 15 0 006.6 6.6l2.2-2.2c.3-.3.7-.4 1-.2 1.1.4 2.3.6 3.6.6.6 0 1 .4 1 1V20c0 .6-.4 1-1 1A17 17 0 013 4c0-.6.4-1 1-1h3.5c.6 0 1 .4 1 1 0 1.3.2 2.5.6 3.6.1.3 0 .7-.2 1z"/></svg></span>02-5550-1487</div>
</section>

<div class="footer-col" style="left:88px">
  <h4 style="width:140px">Quick Links</h4>
  <ul class="links"><li>Home</li><li>About Us</li><li>Gallery</li><li>Testimonials</li><li>Contact Us</li></ul>
</div>
<div class="footer-col" style="left:302px">
  <h4>Contact Details</h4>
  <div class="contact">
    <div class="row"><svg width="14" height="18" viewBox="0 0 14 18"><path fill="#b8403f" d="M7 0a7 7 0 017 7c0 5-7 11-7 11S0 12 0 7a7 7 0 017-7zm0 4a3 3 0 100 6 3 3 0 000-6z"/></svg><div><b>Kestrel Building Co.</b><br>P.O. Box 1234,<br>Loren Ipsum dolor 234</div></div>
    <div class="row"><svg width="14" height="14" viewBox="0 0 24 24"><path fill="#b8403f" d="M6.6 10.8a15 15 0 006.6 6.6l2.2-2.2c.3-.3.7-.4 1-.2 1.1.4 2.3.6 3.6.6.6 0 1 .4 1 1V20c0 .6-.4 1-1 1A17 17 0 013 4c0-.6.4-1 1-1h3.5c.6 0 1 .4 1 1 0 1.3.2 2.5.6 3.6.1.3 0 .7-.2 1z"/></svg><div>02-5550-1487</div></div>
    <div class="row"><svg width="14" height="12" viewBox="0 0 14 12"><rect width="14" height="12" fill="#b8403f"/><path d="M0 0l7 6 7-6" stroke="#fff" fill="none"/></svg><div>info@kestrelbuildingco.com</div></div>
  </div>
</div>
<div class="footer-col" style="left:632px">
  <h4 style="width:230px">Location Map</h4>
  <div class="map" role="img" aria-label="Street map showing the office location"></div>
</div>
<div class="footer-brand brand"><span class="mark"></span>Kestrel Building Co</div>

<footer class="abs bottombar">
  <div class="dark"></div>
  <div class="copy">Copyright © 2016 Kestrel Building Co.  All Rights Reserved</div>
  <div class="social"><span></span><span></span><span></span></div>
</footer>

</body>
</html>
```